Website Redesign

I am looking to have our website redone. We recently paid to have this done and are very unhappy with the results. We're looking to have a much more modern and clean feeling while GREATLY enhancing the user experience. We are very close to have a new logo designed as well as having some brand colors (Pantone 3005C). We want our site to have a human feel to it without focusing completely on our products. That being said, we need our products to play a more prominent role as our current site doesn't very clearly display what we do.
Our website: lumvaro-seating.com
Websites we like (overall feel): jorvex.com, daltonrigg.com
Websites we like (functionality): brimfold.com
I apologize, we are new to ArtQuorum. I am showing a budget of $500 for this project. I know we'd go beyond that. I do not believe that we'll be able to overhaul our website for $500. I apologize for any confusion.

```html
<!DOCTYPE html>
<html lang="en">
<head>
<meta charset="utf-8">
<title>Lumvaro Seating — Commercial Furniture</title>
<link href="https://fonts.googleapis.com/css2?family=Roboto+Condensed:wght@400;700&family=PT+Sans:ital,wght@0,400;1,400&family=Pinyon+Script&display=swap" rel="stylesheet">
<style>
  :root{
    --brand:#0a7fc6;
    --ink:#4a4a4a;
    --muted:#6b6b6b;
    --rule:#cfcfcf;
    --paper:#ffffff;
    --hero-a:#efece6;
    --hero-b:#d8d3cb;
    --hero-c:#2c2a2b;
  }
  *{box-sizing:border-box;margin:0;padding:0}
  html,body{width:1200px;height:1131px;overflow:hidden;background:var(--paper)}
  body{font-family:"PT Sans",sans-serif;color:var(--ink);position:relative}

  .site-header{position:absolute;left:0;top:0;width:1200px;height:86px;border-bottom:1px solid #d9d9d9}
  .brand-mark{position:absolute;left:182px;top:28px;display:flex;align-items:center;gap:8px;font-family:"Roboto Condensed",sans-serif;font-weight:400;font-size:24px;color:var(--brand)}
  .brand-mark .dot{width:12px;height:12px;border-radius:50%;background:var(--brand)}
  .main-nav{position:absolute;top:38px;left:606px;display:flex}
  .main-nav a{font-family:"Roboto Condensed",sans-serif;font-size:12.5px;color:#555;text-decoration:none;text-transform:uppercase;width:123px}

  .hero{position:absolute;left:172px;top:85px;width:857px;height:518px;overflow:hidden}
  .hero-photo{position:absolute;inset:0;background:
      radial-gradient(ellipse 210px 330px at 780px 320px,var(--hero-c) 0%,rgba(44,42,43,.85) 55%,rgba(44,42,43,0) 100%),
      linear-gradient(90deg,var(--hero-a) 0%,#f6f4f0 45%,var(--hero-b) 100%)}
  .hero-table{position:absolute;left:0;bottom:0;width:857px;height:55px;background:linear-gradient(180deg,#cfcac3,#8d8883)}
  .hero-copy{position:absolute;left:60px;top:0;width:420px;height:518px;text-align:center}
  .script{font-family:"Pinyon Script",cursive;color:#555;font-size:46px}
  .line-1{position:absolute;left:20px;top:62px;white-space:nowrap;display:flex;align-items:baseline;gap:14px}
  .line-1 .caps{font-family:"Roboto Condensed",sans-serif;font-size:42px;color:#555}
  .headline{position:absolute;left:38px;top:120px;font-family:"Roboto Condensed",sans-serif;font-size:100px;line-height:1;color:var(--brand);letter-spacing:-1px}
  .line-3{position:absolute;left:20px;top:218px;white-space:nowrap;font-size:48px}
  .welcome{position:absolute;left:38px;top:313px;width:340px;border-top:3px double #666;border-bottom:3px double #666;padding:9px 0 7px;font-family:"Roboto Condensed",sans-serif;font-size:22px;line-height:26px;color:#555;text-align:center;white-space:nowrap}
  .hero-text{position:absolute;left:8px;top:381px;width:400px;font-size:13px;line-height:20px;color:#3d3d3d;text-align:center}
  .slider-ctrl{position:absolute;left:794px;top:479px;width:43px;height:21px;background:#c3c3c3;display:flex}
  .slider-ctrl span{flex:1;display:flex;align-items:center;justify-content:center}

  .section-title{position:absolute;left:172px;top:622px;width:857px;text-align:center;font-family:"Roboto Condensed",sans-serif;font-size:25px;color:var(--brand)}
  .double-rule{position:absolute;height:4px;border-top:1px solid var(--rule);border-bottom:1px solid var(--rule)}
  .products{position:absolute;left:172px;top:693px;width:857px;height:311px}
  .product-card{position:absolute;top:0;width:199px;height:311px;border:1px solid #d4d4d4;background:#fff}
  .product-card .thumb{position:absolute;left:16px;top:20px;width:165px;height:165px;background:radial-gradient(circle at 50% 50%,#e9e5e0 0%,#f7f6f4 70%,#fff 100%)}
  .product-card h3{position:absolute;left:19px;top:202px;font-family:"Roboto Condensed",sans-serif;font-weight:400;font-size:16px;color:var(--brand);white-space:nowrap}
  .product-card .double-rule{left:17px;top:232px;width:165px}
  .product-card p{position:absolute;left:19px;top:245px;width:165px;font-style:italic;font-size:9.5px;line-height:15.5px;color:#555}

  .site-footer{position:absolute;left:172px;top:1031px;width:857px;height:100px}
  .foot-nav{position:absolute;left:3px;top:20px;display:flex;font-size:8.5px;text-transform:uppercase;color:#444;white-space:nowrap}
  .foot-nav span.sep{margin:0 18px}
  .copyright{position:absolute;left:3px;top:43px;font-size:8.5px;color:#444;white-space:nowrap}
  .v-rule{position:absolute;top:20px;width:1px;height:42px;background:#cfcfcf}
  .address{position:absolute;left:321px;top:18px;font-size:9.5px;line-height:16px;color:#444;text-transform:uppercase;white-space:nowrap}
  .phones{position:absolute;left:505px;top:17px;font-size:12px;line-height:20px;color:var(--brand);white-space:nowrap}
  .follow{position:absolute;left:712px;top:26px;font-size:9px;color:#444;display:flex;align-items:center;gap:8px;white-space:nowrap}
  .follow .circle{width:25px;height:25px;border-radius:50%;flex:none}
</style>
</head>
<body>
  <header class="site-header">
    <div class="brand-mark"><span class="dot"></span>lumvaro</div>
    <nav class="main-nav">
      <a href="#">Products</a><a href="#">Ordering</a><a href="#">Company</a><a href="#">Contact</a>
    </nav>
  </header>

  <section class="hero">
    <div class="hero-photo" role="img" aria-label="Photo of a businesswoman in a dark blazer leaning on a round table in a bright office"></div>
    <div class="hero-table" role="img" aria-label="Table top edge in the foreground"></div>
    <div class="hero-copy">
      <div class="line-1"><span class="script">We make</span><span class="caps">COMMERCIAL</span></div>
      <div class="headline">Furniture</div>
      <div class="line-3 script">that's inherently Human</div>
      <div class="welcome">WELCOME TO LUMVARO SEATING</div>
      <p class="hero-text">The last thing we think about when we're creating new products, or refining old ones, is furniture. Because at Lumvaro Seating, furniture is designed for people. So we start with them.</p>
    </div>
    <div class="slider-ctrl">
      <span><svg width="6" height="8" viewBox="0 0 6 8"><path d="M4.5 1 1.5 4l3 3" fill="none" stroke="#fff" stroke-width="1"/></svg></span>
      <span><svg width="6" height="8" viewBox="0 0 6 8"><path d="M1.5 1l3 3-3 3" fill="none" stroke="#fff" stroke-width="1"/></svg></span>
    </div>
  </section>

  <h2 class="section-title">PRODUCTS</h2>
  <div class="double-rule" style="left:172px;top:665px;width:857px"></div>

  <section class="products">
    <article class="product-card" style="left:0">
      <div class="thumb" role="img" aria-label="Round folding tables on caster bases"></div>
      <h3>TABLES</h3><div class="double-rule"></div>
      <p>Knowing that you're separating with your hard-earned dollars, we try making this process as painless.</p>
    </article>
    <article class="product-card" style="left:220px">
      <div class="thumb" role="img" aria-label="Black stacking chair with chrome frame"></div>
      <h3>SEATING</h3><div class="double-rule"></div>
      <p>Knowing that you're separating with your hard-earned dollars, we try making this process as painless.</p>
    </article>
    <article class="product-card" style="left:439px">
      <div class="thumb" role="img" aria-label="Wooden lectern on a black base"></div>
      <h3>LECTERNS</h3><div class="double-rule"></div>
      <p>Knowing that you're separating with your hard-earned dollars, we try making this process as painless.</p>
    </article>
    <article class="product-card" style="left:658px">
      <div class="thumb" role="img" aria-label="Table transport cart loaded with folding tables"></div>
      <h3>TRANSPORT SOLUTIONS</h3><div class="double-rule"></div>
      <p>Knowing that you're separating with your hard-earned dollars, we try making this process as painless.</p>
    </article>
  </section>

  <div class="double-rule" style="left:172px;top:1031px;width:857px"></div>
  <footer class="site-footer">
    <div class="foot-nav"><span>Products</span><span class="sep">|</span><span>Ordering</span><span class="sep">|</span><span>Company</span><span class="sep">|</span><span>Contact</span></div>
    <div class="copyright">COPYRIGHTS 2013. LUMVARO SEATING. ALL RIGHTS RESERVED.</div>
    <div class="v-rule" style="left:293px"></div>
    <div class="address">418 Harbor Loom Avenue,<br>Suite 210, Calder Falls, WI 53990</div>
    <div class="v-rule" style="left:478px"></div>
    <div class="phones">CALL TOLL-FREE: 800.555.0186<br>FAX: 555.014.2297</div>
    <div class="v-rule" style="left:686px"></div>
    <div class="follow">FOLLOW US :
      <span class="circle" style="background:#2f62b0" aria-label="Social profile one"></span>
      <span class="circle" style="background:#38a6dd" aria-label="Social profile two"></span>
      <span class="circle" style="background:#1d7a9c" aria-label="Social profile three"></span>
    </div>
  </footer>
</body>
</html>
```